K9 Orbit needs a business card designed

We need a business card designed for K9 Orbit, an expansion of K9 Systems Pty Ltd (www.k9systems.com.au)

We provide high quality professional services for the Australian space industry. Our clients include the Southern Launch Bureau and companies working in the space industry. We identify people with space related skills both locally and internationally who are then contracted by clients to create products and support space launch activities.

Colours to be used:
- Navy blue #000080
- Rocket metallic #8A7F8D
- Platinum #E5E4E2
- Black #000000
- White #FFFFFF

*Front of the card*
I have attached our K9 Orbit logo, which needs to be the main item on the card. The 'Space' text should be placed to the right of the 'K9' part rather than below, similar to the attached K9 Systems card, which this card should match.

If subtext is included, however, it should read ‘Labour Hire • Consultancy • Project Delivery’ rather than the ‘Design • Build • Test • Maintain’ of the K9 Systems card.

A black background (rather than blue background in the K9 Systems card) might be good, with a white pattern as in the K9 Systems card. If colour is used, the logo should be in its standard colours (as provided for the K9 Orbit logo).

*Back of the card*
Include a smaller K9 Orbit logo on the back.

We need the following details for K9 Orbit personnel (as a template for entry):
- Name
- Company Position
- Mobile Number
- Email
- Office Address
- Include the K9 Orbit website: www.k9orbit.com.au

Overall, we'd like to see a design that communicates the adventure of space, professional integrity, and customer service. We look forward to seeing what you can come up with.

Target Market(s)

We provide high quality professional services for the Australian space industry. Our clients include the Southern Launch Bureau and companies working in the space industry.

Contact Information for Business Card

- Name
- Company Position
- Mobile Number
- Email
- Office Address

Requirements
Must have
• See project description.

```html
<!DOCTYPE html>
<html lang="en">
<head>
<meta charset="utf-8">
<title>K9 Orbit Business Card</title>
<link href="https://fonts.googleapis.com/css2?family=Quicksand:wght@400;500;600;700&display=swap" rel="stylesheet">
<style>
  :root {
    --navy: #272872;
    --ink: #45444a;
    --muted: #8a7f8d;
    --white: #ffffff;
    --backdrop: #e5e4e2;
    --rule: #8c8c8c;
  }
  * { margin: 0; padding: 0; box-sizing: border-box; }
  html, body {
    width: 1200px; height: 1200px; overflow: hidden;
    background: var(--backdrop);
    font-family: "Quicksand", sans-serif;
  }
  .card {
    position: absolute; left: 244px; width: 712px; height: 407px;
    box-shadow: 6px 8px 14px rgba(0,0,0,0.35);
  }
  .card-front { top: 158px; background: var(--white); }
  .card-front .base-band {
    position: absolute; left: 0; right: 0; bottom: 0; height: 7px; background: var(--navy);
  }
  .brand { position: absolute; }
  .brand-name {
    display: block; font-weight: 600; letter-spacing: 0; white-space: nowrap; line-height: 1;
  }
  .tagline { position: absolute; white-space: nowrap; font-weight: 500; letter-spacing: 0.01em; }
  .card-front .brand { left: 56px; top: 172px; }
  .card-front .brand-name { font-size: 42px; color: var(--navy); }
  .card-front .tagline { left: 56px; top: 222px; font-size: 8.5px; color: var(--muted); }
  .divider {
    position: absolute; left: 393px; top: 100px; width: 1px; height: 207px; background: var(--rule);
  }
  .contact { position: absolute; left: 416px; top: 101px; color: var(--ink); }
  .person-name { font-size: 22px; font-weight: 700; color: var(--navy); line-height: 26px; }
  .person-role { font-size: 16.5px; line-height: 22px; letter-spacing: 0.03em; }
  .address { margin-top: 16px; font-size: 16.5px; line-height: 20.5px; letter-spacing: 0.04em; font-style: normal; }
  .channels { list-style: none; margin-top: 14px; font-size: 16.5px; letter-spacing: 0.05em; }
  .channels li { display: flex; align-items: center; height: 22px; }
  .channels svg { width: 15px; height: 15px; margin-right: 13px; flex: none; }
  .card-back { top: 617px; background: var(--navy); }
  .card-back .brand { left: 126px; top: 155px; }
  .card-back .brand-name { font-size: 68px; color: var(--white); }
  .card-back .tagline { left: 298px; top: 233px; font-size: 13.5px; color: var(--white); }
</style>
</head>
<body>
  <section class="card card-front" aria-label="Card front">
    <div class="brand">
      <span class="brand-name">K9 Orbit</span>
    </div>
    <p class="tagline">Labour Hire • Consultancy • Project Delivery</p>
    <div class="divider"></div>
    <div class="contact">
      <h1 class="person-name">MARCO ELLISON</h1>
      <p class="person-role">Director</p>
      <address class="address">Level 2, 48 Harbour St<br>Port Ashby<br>VIC 3999</address>
      <ul class="channels">
        <li><svg viewBox="0 0 16 16" aria-hidden="true"><path fill="#272872" d="M3.6 1.2l2.3 2.6-1.3 1.9c.9 2 2.4 3.5 4.4 4.4l1.9-1.3 2.6 2.3-1.2 2.3C7 13.2 2.8 9 1.3 2.4z"/></svg>000 000 0000</li>
        <li><svg viewBox="0 0 16 16" aria-hidden="true"><rect x="1.5" y="3.5" width="13" height="9" rx="1" fill="none" stroke="#272872" stroke-width="1.6"/><path d="M2 4.5l6 4.5 6-4.5" fill="none" stroke="#272872" stroke-width="1.6"/></svg>info@k9orbit.com.au</li>
        <li><svg viewBox="0 0 16 16" aria-hidden="true"><g fill="none" stroke="#272872" stroke-width="1.3"><circle cx="8" cy="8" r="6.5"/><ellipse cx="8" cy="8" rx="3" ry="6.5"/><path d="M1.5 8h13M2.5 4.8h11M2.5 11.2h11"/></g></svg>www.k9orbit.com.au</li>
      </ul>
    </div>
    <div class="base-band"></div>
  </section>

  <section class="card card-back" aria-label="Card back">
    <div class="brand">
      <span class="brand-name">K9 Orbit</span>
    </div>
    <p class="tagline">Labour Hire • Consultancy • Project Delivery</p>
  </section>
</body>
</html>
```